Web Design For Staffing Company

We need a homepage web design for a technical staffing company.

Please see attached brief for project details.

please make the site modern with bold colors while matching the logo

Be sure to read the attached breif in full beforehand.

Target Market(s)

technical companies looking to hire talent

Industry/Entity Type

Staffing

Number of Pages Required

1 page

Font styles to use
Sans Serif

```html
<!DOCTYPE html>
<html lang="en">
<head>
<meta charset="utf-8">
<title>Veltrix Staffing</title>
<link href="https://fonts.googleapis.com/css2?family=Mulish:wght@400;600;700&family=Montserrat:wght@500;600;700&display=swap" rel="stylesheet">
<style>
:root{
  --blue:#2b7bc0;
  --blue-light:#3b8fd6;
  --navy:#1b4a72;
  --ink:#222;
  --muted:#555;
  --band:#eef3f8;
  --footer:#0e0e0e;
  --bar:#2a6fb2;
  --white:#fff;
}
*{box-sizing:border-box;margin:0;padding:0}
html,body{width:1200px;height:3636px;overflow:hidden}
body{position:relative;font-family:"Mulish",sans-serif;color:var(--ink);background:var(--white)}
.abs{position:absolute}
.btn{position:absolute;display:flex;align-items:center;justify-content:center;color:#fff;font-family:"Mulish",sans-serif;font-weight:600;font-size:15px}
.btn-blue{background:var(--blue)}
.btn-navy{background:var(--navy)}
.btn-black{background:#000}
.card{position:absolute;background:#fff;box-shadow:0 4px 16px rgba(0,0,0,.12)}
.photo{position:absolute}

/* header */
.site-header{position:absolute;top:0;left:0;width:1200px;height:84px;background:#fff}
.brand{position:absolute;left:141px;top:20px;display:flex;align-items:center;gap:10px;font-family:"Montserrat",sans-serif;font-weight:700;font-size:30px;color:var(--navy)}
.brand-dot{width:34px;height:34px;border-radius:50%;background:var(--blue)}
.nav{position:absolute;top:18px;left:460px;display:flex;gap:34px}
.nav-item{display:flex;flex-direction:column;align-items:center;gap:6px;font-size:12.5px;color:#333;font-family:"Mulish",sans-serif}
.nav-item.active{color:var(--blue);text-decoration:underline}
.search{position:absolute;left:925px;top:21px;width:133px;height:35px;border:1px solid #ccc;border-radius:3px;font-size:12px;color:#555;padding:10px 8px}
.search svg{position:absolute;right:7px;top:11px}

/* hero */
.hero{left:0;top:84px;width:1200px;height:579px;background:linear-gradient(180deg,#8a8f96 0%,#5b5f66 55%,#2a2c30 100%)}
.hero-title{position:absolute;top:434px;left:0;width:1200px;text-align:center;font-family:"Montserrat",sans-serif;font-weight:700;font-size:32px;line-height:50px;color:#fff}

.intro{left:141px;top:620px;width:918px;height:173px;text-align:center;font-size:18.5px;line-height:33px;padding:37px 60px}

.copy{font-size:17.4px;line-height:30.5px;color:#222}
.copy .lead{color:var(--blue);font-weight:600}

/* testimonials */
.band{left:0;top:1892px;width:1200px;height:494px;background:var(--band)}
.section-title{position:absolute;left:0;width:1200px;text-align:center;font-family:"Montserrat",sans-serif;font-weight:600;font-size:28px;color:#111}
.quote-text{position:absolute;left:454px;top:2060px;width:425px;font-size:12.6px;line-height:25.5px;color:#333}
.dot{position:absolute;top:2292px;width:14px;height:14px;border-radius:50%;border:1px solid var(--blue);background:#fff}

/* blogs */
.post{position:absolute;top:2526px;width:293px;height:399px;background:#fff;box-shadow:0 3px 12px rgba(0,0,0,.1)}
.post-img{height:187px}
.post-body{padding:12px 18px}
.meta{font-size:11px;color:#444;display:flex;gap:8px;align-items:center}
.post-title{margin-top:10px;font-size:16.5px;line-height:24px;color:#222;font-weight:600}
.excerpt{margin-top:8px;font-size:11px;line-height:20px;color:#444}
.read{display:inline-block;margin-top:10px;font-size:12.5px;color:var(--navy);text-decoration:underline;font-weight:600}

/* cta */
.cta{position:absolute;top:3073px;width:445px;height:212px;background:linear-gradient(135deg,rgba(43,123,192,.92),rgba(58,140,210,.88));text-align:center;color:#fff}
.cta h3{margin-top:84px;font-family:"Mulish",sans-serif;font-weight:600;font-size:22px;line-height:31px}

/* footer */
.footer{left:0;top:3235px;width:1200px;height:361px;background:var(--footer)}
.f-title{position:absolute;top:3362px;color:#fff;font-size:17px;font-weight:600}
.f-text{position:absolute;color:#ddd;font-size:12px;line-height:23px}
.f-btn{position:absolute;top:3500px;width:120px;height:31px;background:var(--blue);color:#fff;font-size:12.5px;display:flex;align-items:center;justify-content:center;gap:6px}
.f-brand{position:absolute;left:840px;top:3430px;display:flex;align-items:center;gap:12px;color:#fff;font-family:"Montserrat",sans-serif;font-weight:700;font-size:40px}
.f-brand .sq{width:40px;height:40px;border-radius:50%;background:#fff}
.bar{left:0;top:3596px;width:1200px;height:40px;background:var(--bar);color:#fff;font-size:12px}
.social{position:absolute;top:10px;width:22px;height:22px;border:1.5px solid #fff;border-radius:50%}
</style>
</head>
<body>

<header class="site-header">
  <div class="brand"><span class="brand-dot"></span>Veltrix</div>
  <nav class="nav">
    <div class="nav-item active"><svg width="16" height="16"><path d="M2 8l6-5.5L14 8M4 7v7h8V7" stroke="#2b7bc0" stroke-width="1.5" fill="none"/></svg>HOME</div>
    <div class="nav-item"><svg width="16" height="16"><circle cx="8" cy="7" r="4.5" stroke="#333" fill="none"/><path d="M6 12h4M6 14h4" stroke="#333"/></svg>ABOUT</div>
    <div class="nav-item"><svg width="16" height="16"><circle cx="10" cy="6" r="4" stroke="#333" fill="none"/><path d="M7 9l-5 5" stroke="#333" stroke-width="1.5"/></svg>JOB SEEKERS</div>
    <div class="nav-item"><svg width="16" height="16"><circle cx="8" cy="5" r="3.5" stroke="#333" fill="none"/><path d="M2 15q6-9 12 0" stroke="#333" fill="none"/></svg>CLIENTS</div>
    <div class="nav-item"><svg width="16" height="16"><rect x="3" y="2" width="10" height="12" stroke="#333" fill="none"/><path d="M5 6h6M5 9h6" stroke="#333"/></svg>CONTACT US</div>
  </nav>
  <div class="search">Search<svg width="11" height="11"><circle cx="4.5" cy="4.5" r="3.5" stroke="#333" fill="none" stroke-width="1.5"/><path d="M7 7l3.5 3.5" stroke="#333" stroke-width="1.5"/></svg></div>
</header>

<section>
  <div class="photo hero" role="img" aria-label="Team of professionals in discussion around an office table"></div>
  <h1 class="hero-title">The Right People For The Right Jobs!<br>Bridging The Talent Gap In Technical Staffing</h1>
  <a class="btn btn-blue" style="left:456px;top:549px;width:134px;height:42px;font-size:16px">Hire Talent</a>
  <a class="btn btn-blue" style="left:610px;top:549px;width:134px;height:42px;font-size:16px">Get Hired</a>
  <div class="card intro">Veltrix Staffing is a National Technical Staffing and Recruiting Solutions Provider founded in 2013 focused on matching contract and full time Engineering and IT professionals with new andexciting employment opportunities!</div>
</section>

<section>
  <div class="photo" style="left:141px;top:867px;width:537px;height:394px;background:linear-gradient(135deg,#c9d3dc,#8f9aa4)" role="img" aria-label="Smiling colleagues meeting at a glass table"></div>
  <div class="card" style="left:522px;top:979px;width:537px;height:324px;padding:42px 28px 0 38px">
    <p class="copy"><span class="lead">We Love To Recruit!</span>&nbsp; It’s our passion and we take it very seriously! It is noteasy for JOB SEEKERS to put their job search efforts and trust in the hands of someone else, especially when there are so many Staffing Firms to choose from. So how do you know you arechoosing the best Staffing Representation possible?</p>
  </div>
  <a class="btn btn-blue" style="left:560px;top:1218px;width:127px;height:37px">Learn More</a>
  <a class="btn btn-navy" style="left:697px;top:1218px;width:127px;height:37px">View Jobs</a>

  <div class="photo" style="left:522px;top:1375px;width:536px;height:395px;background:linear-gradient(135deg,#7d8f9f,#d9d2c8)" role="img" aria-label="Businesswoman smiling during a conversation with a colleague"></div>
  <div class="card" style="left:141px;top:1487px;width:537px;height:324px;padding:24px 22px 0 38px">
    <p class="copy">Are you responsible for Technical Staffing within your organization?&nbsp; Are you satisfied with yourcurrent Supplier(s)’ overall performance?<br>Does it appear they identify potential Candidate(s)based purely on “buzz-word” searches?&nbsp; Is it evident they just do not grasp the scope andresponsibilities of your technical staffing need(s)?</p>
  </div>
  <a class="btn btn-blue" style="left:175px;top:1744px;width:127px;height:37px">Learn More</a>
  <a class="btn btn-navy" style="left:313px;top:1744px;width:127px;height:37px">Hire Talent</a>
</section>

<section>
  <div class="abs band"></div>
  <h2 class="section-title" style="top:1958px">Testimonials</h2>
  <div class="card" style="left:310px;top:2040px;width:580px;height:230px;box-shadow:0 2px 8px rgba(0,0,0,.06)"></div>
  <div class="card" style="left:282px;top:2030px;width:635px;height:225px"></div>
  <svg class="abs" style="left:344px;top:2072px" width="72" height="72"><circle cx="36" cy="36" r="35" fill="#d9d9d9"/><circle cx="36" cy="30" r="12" fill="#fff" stroke="#222" stroke-width="3"/><path d="M14 64q22-22 44 0" fill="#fff" stroke="#222" stroke-width="3"/></svg>
  <div class="abs" style="left:333px;top:2154px;color:#f39c12;font-size:15px;letter-spacing:2px">★★★★★</div>
  <p class="quote-text">Mark Devlin is an excellent recruiter. He is articulate, honest, has a good nature and is aneffective information conduit between his clients and candidates. He gave me the feeling he is there for the big picture desiring to forge a future relationship that will be mutually beneficial toboth of us.</p>
  <div class="abs" style="left:454px;top:2193px;font-size:13px"><b style="font-size:14px">Sam K</b> <span style="font-size:11px">- Electrical Test Engineer in the Automotive Sector</span></div>
  <div class="abs" style="left:845px;top:2180px;font-family:Georgia,serif;font-size:90px;color:#ddd;line-height:1">“</div>
  <span class="dot" style="left:571px"></span>
  <span class="dot" style="left:592px"></span>
  <span class="dot" style="left:613px;background:var(--blue);box-shadow:inset 0 0 0 3px #fff"></span>
</section>

<section>
  <h2 class="section-title" style="top:2455px">Latest Blogs</h2>
  <article class="post" style="left:141px">
    <div class="post-img" style="background:linear-gradient(135deg,#c6cfd8,#5e6d7d)" role="img" aria-label="Woman typing on a laptop"></div>
    <div class="post-body">
      <div class="meta"><span>▭ June 17, 2019</span><span>|</span><span>by veltrixstaffing</span></div>
      <h3 class="post-title">Ways To Make The Most Of The Hot Job Market</h3>
      <p class="excerpt">This is the tightest labor market I can remember. Unemployment is at a 50-year low and wage growth is at 3.2%,” said...[+]</p>
      <a class="read">Read More</a>
    </div>
  </article>
  <article class="post" style="left:453px">
    <div class="post-img" style="background:linear-gradient(135deg,#9fc3e4,#1f3f66)" role="img" aria-label="Business handshake"></div>
    <div class="post-body">
      <div class="meta"><span>▭ June 6, 2019</span><span>|</span><span>by veltrixstaffing</span></div>
      <h3 class="post-title">Back To Basics: Meeting Employees’ Needs To Improve Organizational Performance</h3>
      <p class="excerpt">The benefits of employee satisfaction are well-established, so HR professionals...[+]</p>
      <a class="read">Read More</a>
    </div>
  </article>
  <article class="post" style="left:765px">
    <div class="post-img" style="background:linear-gradient(135deg,#6e6e6e,#151515)" role="img" aria-label="Black and white portrait with a quote about technology"></div>
    <div class="post-body">
      <div class="meta"><span>▭ May 20, 2019</span><span>|</span><span>by veltrixstaffing</span></div>
      <h3 class="post-title">5 Important Takeaways From Nimbus’s Two-Year Study Of Remote Work</h3>
      <p class="excerpt">Recently, the folks at Nimbus published their findings from a two-year study...[+]</p>
      <a class="read">Read More</a>
    </div>
  </article>
  <a class="btn btn-navy" style="left:536px;top:2963px;width:127px;height:37px">View All</a>
</section>

<section>
  <div class="abs footer"></div>
  <div class="cta" style="left:141px" role="img" aria-label="Blue-tinted photo of a job candidate">
    <svg class="abs" style="left:185px;top:28px" width="76" height="52"><g stroke="#fff" stroke-width="2" fill="none"><circle cx="38" cy="14" r="10"/><path d="M20 50q18-26 36 0"/><circle cx="14" cy="24" r="7"/><circle cx="62" cy="24" r="7"/><path d="M2 50q12-18 22-6M74 50q-12-18-22-6"/></g></svg>
    <h3>Looking For Career-Minded<br>Candidates?</h3>
    <a class="btn btn-black" style="left:152px;top:152px;width:141px;height:36px">Request Talent</a>
  </div>
  <div class="cta" style="left:614px" role="img" aria-label="Blue-tinted photo of professionals at work">
    <svg class="abs" style="left:198px;top:26px" width="52" height="56"><g stroke="#fff" stroke-width="2" fill="none"><circle cx="22" cy="14" r="10"/><path d="M4 52q18-26 36 0"/><rect x="28" y="32" width="20" height="14"/></g></svg>
    <h3>Looking For Career<br>Opportunities?</h3>
    <a class="btn btn-black" style="left:152px;top:150px;width:141px;height:36px">Search Jobs</a>
  </div>

  <h4 class="f-title" style="left:142px">Find Jobs</h4>
  <p class="f-text" style="left:142px;top:3394px;width:160px">Search Our extensive list of available jobs to find your match.</p>
  <h4 class="f-title" style="left:345px">Request An Employee</h4>
  <p class="f-text" style="left:346px;top:3394px;width:200px">We’re here to provide the people you need to get work done.</p>
  <h4 class="f-title" style="left:584px">Get In Touch</h4>
  <svg class="abs" style="left:582px;top:3400px" width="12" height="15"><path d="M6 14q-5-6-5-9a5 5 0 0110 0q0 3-5 9z" fill="#fff"/><circle cx="6" cy="5" r="2" fill="#000"/></svg>
  <p class="f-text" style="left:602px;top:3394px;width:180px;line-height:18px">220 Harbor Road, Bldg. 3, 1st floor Lakeview, MA 01990</p>
  <svg class="abs" style="left:582px;top:3462px" width="12" height="12"><path d="M2 1l3 0 1 3-2 1q1 3 4 4l1-2 3 1 0 3q-11 0-10-10z" fill="#fff"/></svg>
  <p class="f-text" style="left:602px;top:3457px">555-014-2290</p>

  <div class="f-btn" style="left:141px"><svg width="11" height="11"><circle cx="4.5" cy="4.5" r="3.5" stroke="#fff" fill="none" stroke-width="1.5"/><path d="M7 7l3.5 3.5" stroke="#fff" stroke-width="1.5"/></svg>Search Now</div>
  <div class="f-btn" style="left:347px"><svg width="11" height="11"><circle cx="5.5" cy="3" r="2.8" fill="#fff"/><path d="M0 11q5.5-8 11 0z" fill="#fff"/></svg>Start Today</div>
  <div class="f-btn" style="left:580px"><svg width="12" height="9"><rect x=".5" y=".5" width="11" height="8" fill="#fff"/><path d="M.5 .5l5.5 4 5.5-4" stroke="#2b7bc0" fill="none"/></svg>Contact Us</div>

  <div class="f-brand"><span class="sq"></span>Veltrix</div>

  <div class="abs bar">
    <span class="abs" style="left:142px;top:13px">Copyright © 2020 Veltrix Staffing. All Rights Reserved.</span>
    <span class="social" style="left:965px"></span>
    <span class="social" style="left:999px"></span>
    <span class="social" style="left:1034px"></span>
  </div>
</section>

</body>
</html>
```